Moderne Visitenkarten für Medizintechnikfirma
Zielgruppe
Vertriebsfirma von moderner und innovativer Medizintechnik
Zielgruppe: Ärzte, Kliniken, Medizintechnikfirmen, Patienten
Aufgabenstellung
Besonderes, modernes, auffälliges und ansprechendes Design ohne überladen oder aufdringlich zu sein
Farbenorientierung kann am Logo und der Website geschehen. Wenn zum Logo harmonierend, sind aber auch andere Farben gerne gesehen.
Format: eher horizontal, vertikal aber auch möglich, abgerundete Ecken einplanen
Wenn möglich folgende Infos bitte schon auf die Karten bringen (pro Person eine Karte):
Harald Zumbrink (CEO)
harald.zumbrink@vitalnova-partner.de
(VitalNova Partner GmbH
Lärchenstraße 14
49377 Fallrode)
www.vitalnova-partner.de
info@vitalnova-partner.de
Jannik Sprau (CoS)
jannik.sprau@vitalnova-partner.de
Die allgemeinen Firmeninfos können deutlich kleiner sein. Anschrift nur wenn es dadurch nicht zu viel werden würde.

```html
<!DOCTYPE html>
<html lang="de">
<head>
<meta charset="utf-8">
<title>VitalNova Partner – Visitenkarten</title>
<link href="https://fonts.googleapis.com/css2?family=Montserrat:wght@400;500;600&display=swap" rel="stylesheet">
<style>
  :root {
    --bg: #0a2247;
    --bg-edge: #021328;
    --card: #ffffff;
    --purple: #2d1a5c;
    --red: #f3260f;
    --grey: #4a4a4a;
    --grey-dark: #333333;
  }
  html, body {
    margin: 0;
    padding: 0;
    width: 1200px;
    height: 1199px;
    overflow: hidden;
  }
  body {
    position: relative;
    background: radial-gradient(ellipse at center, var(--bg) 0%, #072046 55%, var(--bg-edge) 100%);
    font-family: "Montserrat", sans-serif;
  }
  .card {
    position: absolute;
    width: 620px;
    height: 401px;
    background: var(--card);
    border-radius: 14px;
    overflow: hidden;
    box-shadow: 0 20px 50px rgba(0, 0, 0, 0.45);
  }
  /* company side */
  .card--company {
    left: 110px;
    top: 220px;
  }
  .brand {
    position: absolute;
    top: 110px;
    left: 0;
    right: 0;
    display: flex;
    align-items: center;
    justify-content: center;
    gap: 14px;
  }
  .brand__dot {
    width: 22px;
    height: 22px;
    border-radius: 50%;
    background: var(--purple);
  }
  .brand__name {
    font-size: 38px;
    font-weight: 600;
    color: var(--purple);
    letter-spacing: 0.5px;
  }
  .company-info {
    position: absolute;
    left: 64px;
    right: 48px;
    bottom: 66px;
    display: flex;
    justify-content: space-between;
    align-items: flex-end;
    font-size: 15px;
    line-height: 1.45;
    color: var(--grey-dark);
  }
  .company-info p { margin: 0; }
  .company-band {
    position: absolute;
    left: 0;
    right: 0;
    bottom: 0;
    height: 32px;
    background: var(--red);
  }
  /* personal side */
  .card--person {
    left: 470px;
    top: 570px;
  }
  .network-art {
    position: absolute;
    left: 0;
    top: 0;
    width: 220px;
    height: 100%;
  }
  .person {
    position: absolute;
    left: 260px;
    right: 30px;
    top: 110px;
    text-align: center;
  }
  .person__name {
    margin: 0;
    font-size: 38px;
    font-weight: 500;
    color: var(--grey);
  }
  .person__role {
    margin: 2px 0 0;
    font-size: 14px;
    color: var(--grey);
  }
  .person-contact {
    position: absolute;
    left: 262px;
    bottom: 84px;
    font-size: 15px;
    line-height: 1.55;
    color: var(--grey-dark);
  }
  .person-contact p { margin: 0; }
</style>
</head>
<body>
  <section class="card card--company">
    <div class="brand">
      <span class="brand__dot"></span>
      <span class="brand__name">VitalNova Partner</span>
    </div>
    <div class="company-info">
      <div class="company-address">
        <p>VitalNova Partner GmbH</p>
        <p>Lärchenstraße 14</p>
        <p>49377 Fallrode</p>
      </div>
      <div class="company-contact">
        <p>www.vitalnova-partner.de</p>
        <p>info@vitalnova-partner.de</p>
        <p>0800-5519036</p>
      </div>
    </div>
    <div class="company-band"></div>
  </section>

  <section class="card card--person">
    <svg class="network-art" role="img" aria-label="Decorative molecular network graphic in purple, grey and red" viewBox="0 0 220 401" preserveAspectRatio="none">
      <defs>
        <linearGradient id="networkFill" x1="0" y1="0" x2="1" y2="0">
          <stop offset="0" stop-color="#2d1a5c" stop-opacity="0.55"/>
          <stop offset="0.7" stop-color="#2d1a5c" stop-opacity="0.2"/>
          <stop offset="1" stop-color="#ffffff" stop-opacity="0"/>
        </linearGradient>
      </defs>
      <rect width="220" height="401" fill="url(#networkFill)"/>
    </svg>
    <div class="person">
      <h1 class="person__name">Harald Zumbrink</h1>
      <p class="person__role">CEO</p>
    </div>
    <div class="person-contact">
      <p>+4915209847362</p>
      <p>harald.zumbrink@vitalnova-partner.de</p>
    </div>
  </section>
</body>
</html>
```